Velquor Engineering Consulting

We need a website design for a new company based in South Africa called Zendrex Consulting, it is a formidable engineering and consulting company with a background in Electrical and Mechanical design.We adopt a problem-solving methodology which allows us to present our clients with quick and flexible results. We offer complete engineering solutions from consulting, engineering design and even supply of equipment.
Target Market(s)
Government, private sector and public sector
Industry/Entity Type
Engineering Consulting
Number of Pages Required
5+ page
Colors
Designer to choose colors to be used in the design.
Requirements
Must have
- Must match the design of the profile, must enhance the profile look
Nice to have
- lates in terms of website design
Should not have
- Should be clean as the profile, should not deviate from the feel of the profile

```html
<!DOCTYPE html>
<html lang="en">
<head>
<meta charset="utf-8">
<title>Zendrex Consulting</title>
<link rel="stylesheet" href="https://fonts.googleapis.com/css2?family=Lato:wght@400;700;900&family=Open+Sans:wght@400;600&display=swap">
<style>
:root{
  --navy:#0f1d36;
  --navy-mid:#1c3358;
  --steel:#5b6a7c;
  --white:#ffffff;
  --ink:#1b1b1b;
  --grey-line:#c9ced6;
  --sky:#a9dcec;
  --sky-light:#d8eef5;
}
*{box-sizing:border-box;margin:0;padding:0}
html,body{width:1200px;height:3214px;overflow:hidden;background:var(--white)}
body{position:relative;font-family:"Open Sans",Arial,sans-serif;color:var(--ink)}
.abs{position:absolute}
h1,h2,h3,.nav,.btn,.logo{font-family:"Lato",Arial,sans-serif}

/* hero */
.hero{left:0;top:0;width:1200px;height:710px;background:linear-gradient(120deg,#3d4650 0%,#6f7a82 35%,#c9a23c 55%,#4a5561 75%,#1d2a3a 100%)}
.hero-shade{left:0;top:0;width:1200px;height:710px;background:rgba(10,20,35,.35)}
.logo{color:var(--white);font-weight:700;font-size:26px;letter-spacing:1px;display:flex;align-items:center;gap:10px}
.logo .mark{width:14px;height:14px;border:2px solid currentColor}
.nav{left:330px;top:46px;display:flex;gap:26px;color:var(--white);font-size:13px;font-weight:700;line-height:18px;text-transform:uppercase}
.hero-title{left:0;top:250px;width:1200px;text-align:center;color:var(--white);font-size:44px;font-weight:900;line-height:50px;text-transform:uppercase}
.hero-arrow{left:582px;top:410px}

/* about */
.about-title{left:160px;top:778px;font-size:38px;font-weight:900;color:var(--navy);text-transform:uppercase}
.about-text{left:160px;top:842px;width:370px;font-size:16.5px;line-height:27px;color:#333}
.panel{color:var(--white)}
.panel h3{font-size:22px;font-weight:900;text-transform:uppercase;margin-bottom:6px}
.panel p{font-size:15px;line-height:21px;opacity:.8}

/* services */
.services-title{left:0;top:1270px;width:1200px;text-align:center;color:var(--white);font-size:30px;font-weight:900;text-transform:uppercase}
.card{top:1380px;width:284px;height:344px;border:1.5px solid rgba(255,255,255,.6);color:var(--white);text-align:center;padding-top:64px}
.card h3{font-size:19px;font-weight:900;line-height:24px;text-transform:uppercase;margin-bottom:12px}
.card ul{list-style:none;font-size:15.5px;line-height:24.5px}
.card-icon{top:1332px;width:92px;height:92px;border-radius:50%;border:2px solid var(--white);background:var(--navy-mid)}
.card-more{width:38px;height:38px;border-radius:50%;border:2px solid var(--white)}

/* consulting */
.consult-title{left:613px;top:1948px;font-size:35px;font-weight:900;line-height:42px;color:var(--navy);text-transform:uppercase}
.consult-text{left:613px;top:2050px;width:440px;font-size:17px;line-height:27px;color:#333}
.btn{display:flex;align-items:center;justify-content:center;border:2px solid var(--navy);color:var(--navy);font-size:15px;font-weight:700;text-transform:uppercase;background:transparent}

/* contact */
.contact-title{left:0;top:2420px;width:1200px;text-align:center;font-size:33px;font-weight:900;color:var(--navy);text-transform:uppercase}
.field{background:var(--white);font-family:"Lato",Arial,sans-serif;font-size:13px;color:#333;text-transform:uppercase;padding:0 26px;display:flex;align-items:center}
.field.message{align-items:flex-start;padding-top:22px}

/* footer */
.foot-col h4{font-family:"Lato",Arial,sans-serif;font-size:16px;font-weight:900;color:var(--ink);text-transform:uppercase;margin-bottom:10px}
.foot-col li{list-style:none;font-family:"Lato",Arial,sans-serif;font-size:15px;line-height:28px;color:var(--ink)}
.social{display:flex;gap:26px}
.social span{width:16px;height:16px;border-radius:50%;background:var(--navy-mid)}
.divider{left:0;top:3150px;width:1200px;height:1px;background:var(--grey-line)}
.copyright{left:0;top:3170px;width:1200px;text-align:center;font-family:"Lato",Arial,sans-serif;font-size:14px;color:#555}
</style>
</head>
<body>

<!-- hero -->
<div class="abs hero" role="img" aria-label="Photo of an engineer in a hard hat and high-visibility jacket holding a tablet inside an industrial plant"></div>
<div class="abs hero-shade"></div>
<div class="abs logo" style="left:165px;top:44px"><span class="mark"></span>ZENDREX</div>
<nav class="abs nav">
  <span>About</span>
  <span>Zendrex Engineering<br>Products &amp; Services</span>
  <span>Zendrex Consulting<br>Services</span>
  <span>Industries<br>We Serve</span>
  <span>Accreditation<br>Bodies</span>
  <span>Contact Us</span>
</nav>
<h1 class="abs hero-title">Complete Engineering<br>Solutions From<br>Consulting</h1>
<svg class="abs hero-arrow" width="36" height="48" viewBox="0 0 36 48"><path d="M18 2V44M4 30L18 44L32 30" fill="none" stroke="#fff" stroke-width="3"/></svg>
<svg class="abs" style="left:0;top:640px" width="1200" height="72" viewBox="0 0 1200 72">
  <polygon points="0,72 700,12 1200,40 1200,72" fill="#ffffff"/>
  <polygon points="700,12 1200,18 1200,40" fill="#9aa3ad"/>
</svg>

<!-- about -->
<h2 class="abs about-title">About Us</h2>
<p class="abs about-text">Established in 2014, Zendrex Consulting is a formidable engineering and consulting company with a background in Electrical and Mechanical design. We adopt a problem-solving methodology which allows us to present our clients with quick and flexible results. We offer complete engineering solutions from consulting, engineering design and even supply of equipment.</p>

<svg class="abs" style="left:590px;top:770px" width="436" height="142" viewBox="0 0 436 142" role="img" aria-label="Photo of an engineering site behind the vision panel">
  <defs><linearGradient id="gv" x1="0" x2="1"><stop offset="0" stop-color="#1b3560"/><stop offset="1" stop-color="#4f6a8c"/></linearGradient></defs>
  <polygon points="36,0 436,0 436,142 0,142" fill="url(#gv)"/>
</svg>
<div class="abs panel" style="left:660px;top:804px;width:350px">
  <h3>Our Vision</h3>
  <p>We aim to become the preferred engineering design and consulting firm within the South</p>
</div>
<svg class="abs" style="left:540px;top:924px" width="486" height="152" viewBox="0 0 486 152" role="img" aria-label="Photo of engineers on site behind the mission panel">
  <defs><linearGradient id="gm" x1="0" x2="1"><stop offset="0" stop-color="#142a4e"/><stop offset="1" stop-color="#3c5a80"/></linearGradient></defs>
  <polygon points="40,0 486,0 486,152 0,152" fill="url(#gm)"/>
</svg>
<div class="abs panel" style="left:660px;top:964px;width:350px">
  <h3>Our Mission</h3>
  <p>We offer our clients technologically innovative service, allowing us to create high levels</p>
</div>

<!-- services -->
<svg class="abs" style="left:0;top:1170px" width="1200" height="680" viewBox="0 0 1200 680" role="img" aria-label="Photo of electricity pylons and power lines at dusk">
  <defs><linearGradient id="gs" x1="0" y1="0" x2="0" y2="1"><stop offset="0" stop-color="#0f1d36"/><stop offset=".6" stop-color="#1f3558"/><stop offset="1" stop-color="#3d5474"/></linearGradient></defs>
  <polygon points="0,0 700,48 1200,36 1200,640 0,680" fill="url(#gs)"/>
  <polygon points="700,48 1200,36 1200,84" fill="#9aa3ad"/>
  <polygon points="0,620 0,680 520,660" fill="#c9ced6"/>
</svg>
<h2 class="abs services-title">Product &amp; Services</h2>
<svg class="abs" style="left:108px;top:1525px" width="20" height="36" viewBox="0 0 20 36"><path d="M18 2L2 18L18 34" fill="none" stroke="#fff" stroke-width="2"/></svg>
<svg class="abs" style="left:1072px;top:1525px" width="20" height="36" viewBox="0 0 20 36"><path d="M2 2L18 18L2 34" fill="none" stroke="#fff" stroke-width="2"/></svg>

<div class="abs card" style="left:160px">
  <h3>Engineering &amp;<br>Installation</h3>
  <ul><li>Project Management</li><li>Commissioning</li><li>Equipment supply (bulk supply)</li><li>Building services</li><li>Medium Voltage installation</li><li>Overhead lines installation</li></ul>
</div>
<div class="abs card" style="left:458px">
  <h3>Electrical<br>Design</h3>
  <ul><li>Substation Design</li><li>Overhead Line Design</li><li>Interior and Exterior Lighting</li><li>Designs</li><li>Medium and Low voltage</li><li>reticulations design</li></ul>
</div>
<div class="abs card" style="left:761px">
  <h3>Turnkey<br>Electrification</h3>
  <ul><li>Bulk Supply &amp; Connection</li><li>Overhead line designing</li><li>Transformers and Miniature</li><li>Substations</li><li>Power substations</li></ul>
</div>
<div class="abs card-icon" style="left:256px"></div>
<div class="abs card-icon" style="left:554px"></div>
<div class="abs card-icon" style="left:857px"></div>
<svg class="abs" style="left:256px;top:1332px" width="92" height="92" viewBox="0 0 92 92"><circle cx="46" cy="40" r="13" fill="none" stroke="#fff" stroke-width="2"/><path d="M40 54H52M41 60H51" stroke="#fff" stroke-width="2"/></svg>
<svg class="abs" style="left:554px;top:1332px" width="92" height="92" viewBox="0 0 92 92"><circle cx="46" cy="46" r="14" fill="none" stroke="#fff" stroke-width="2"/><circle cx="46" cy="46" r="5" fill="none" stroke="#fff" stroke-width="2"/></svg>
<svg class="abs" style="left:857px;top:1332px" width="92" height="92" viewBox="0 0 92 92"><path d="M28 60H64M34 60V40H58V60M40 40V32M52 40V32" fill="none" stroke="#fff" stroke-width="2"/></svg>
<div class="abs card-more" style="left:283px;top:1671px"></div>
<div class="abs card-more" style="left:581px;top:1671px"></div>
<div class="abs card-more" style="left:884px;top:1671px"></div>
<svg class="abs" style="left:293px;top:1684px" width="18" height="12" viewBox="0 0 18 12"><path d="M2 2L9 9L16 2" fill="none" stroke="#fff" stroke-width="2"/></svg>
<svg class="abs" style="left:591px;top:1684px" width="18" height="12" viewBox="0 0 18 12"><path d="M2 2L9 9L16 2" fill="none" stroke="#fff" stroke-width="2"/></svg>
<svg class="abs" style="left:894px;top:1684px" width="18" height="12" viewBox="0 0 18 12"><path d="M2 2L9 9L16 2" fill="none" stroke="#fff" stroke-width="2"/></svg>

<!-- consulting -->
<svg class="abs" style="left:162px;top:1922px" width="360" height="355" viewBox="0 0 360 355" role="img" aria-label="Photo of a yellow conveyor structure at a mining stockpile under a blue sky">
  <defs><linearGradient id="gh" x1="0" y1="0" x2="0" y2="1"><stop offset="0" stop-color="#3a6fc0"/><stop offset=".55" stop-color="#c9a23c"/><stop offset="1" stop-color="#4b4a48"/></linearGradient></defs>
  <polygon points="90,0 270,0 360,177 270,355 90,355 0,177" fill="url(#gh)"/>
</svg>
<h2 class="abs consult-title">Zendrex Consulting<br>Services</h2>
<p class="abs consult-text">Our consulting arm is focused on developing high-level electrical engineering solutions for our clients. We take a detailed solutions approach to engineering projects in various industries including mining, transport and construction among others.</p>
<div class="abs btn" style="left:610px;top:2205px;width:170px;height:48px">Learn More</div>

<!-- contact -->
<svg class="abs" style="left:0;top:2350px" width="1200" height="532" viewBox="0 0 1200 532" role="img" aria-label="Photo of wind turbines against a pale blue sky">
  <defs><linearGradient id="gc" x1="0" y1="0" x2="0" y2="1"><stop offset="0" stop-color="#9fd8ea"/><stop offset=".7" stop-color="#d8eef5"/><stop offset="1" stop-color="#eef6f8"/></linearGradient></defs>
  <polygon points="0,0 520,26 1200,6 1200,532 0,532" fill="url(#gc)"/>
  <polygon points="0,0 520,26 0,38" fill="#0f1d36"/>
</svg>
<h2 class="abs contact-title">Contact Us</h2>
<div class="abs field" style="left:188px;top:2508px;width:402px;height:47px">First Name</div>
<div class="abs field" style="left:608px;top:2508px;width:402px;height:47px">Last Name</div>
<div class="abs field" style="left:188px;top:2569px;width:402px;height:47px">Email</div>
<div class="abs field" style="left:608px;top:2569px;width:402px;height:47px">Phone</div>
<div class="abs field message" style="left:188px;top:2632px;width:822px;height:100px">Message</div>
<div class="abs btn" style="left:506px;top:2757px;width:170px;height:48px">Submit Now</div>

<!-- footer -->
<div class="abs logo" style="left:178px;top:2968px;color:var(--navy)"><span class="mark"></span>ZENDREX</div>
<div class="abs foot-col" style="left:366px;top:2930px">
  <h4>Company</h4>
  <ul><li>About Us</li><li>Product &amp; Services</li><li>Consulting Services</li></ul>
</div>
<div class="abs foot-col" style="left:580px;top:2930px">
  <h4>Resources</h4>
  <ul><li>Industries we serve</li><li>Accrediation Bodies</li><li>Contact Us</li></ul>
</div>
<div class="abs foot-col" style="left:806px;top:2922px">
  <h4>Contact</h4>
  <ul><li>T: +27 (0) 11 555 0142</li><li>E: info@zendrexcm.com</li><li>14 Marula Lane, Riverbend,</li><li>Sandton, 2191, South Africa</li></ul>
</div>
<div class="abs social" style="left:808px;top:3080px"><span></span><span></span><span></span></div>
<div class="abs divider"></div>
<p class="abs copyright">© 2019 Company Name &nbsp;All right reserved</p>

</body>
</html>
```